Stylish Business Cards Wanted

- DOUBLE SIDED Design Required -

High end, edgy cards for a corporate and personal stylist. Must include logo,
Name: Belinda Forsey
Title: Director and Stylist
telephone : +61 8 8217 4592
email: belinda@thegarbledger.example
website: thegarbledger.example
Tag: Corporate Workwear & Uniform Specialist | Personal Stylist
Would like nice icons for telephone, email, website

Target Market(s)

Businesses wanting stylish uniforms, people wanting stylish wardrobes

Industry/Entity Type

Corporate Workwear Stylist

Contact Information for Business Card

I would like black, white and gold foiling incorporated in the design - possibly a touch of the other colours on my branding guide attached Name: Belinda Forsey Title: Director and Stylist telephone : +61 8 8217 4592 email: belinda@thegarbledger.example website: thegarbledger.example Tag: Corporate Workwear & Uniform Specialist | Personal Stylist Would like nice icons for telephone, email, website

Font styles to use
Other font styles liked:
• Raleway

Colors

Designer to choose colors to be used in the design.

Requirements
Must have
• Gold foil accents

```html
<!DOCTYPE html>
<html lang="en">
<head>
<meta charset="UTF-8">
<title>The Garb Ledger – Business Cards</title>
<link href="https://fonts.googleapis.com/css2?family=Raleway:wght@300;400;600;700;800&display=swap" rel="stylesheet">
<style>
  :root {
    --backdrop: #e4e7e6;
    --card-white: #ffffff;
    --ink: #1b1b1b;
    --gold: #eec643;
    --gold-text: #e0b22e;
    --grey-text: #2a2a2a;
  }
  * { box-sizing: border-box; margin: 0; padding: 0; }
  html, body {
    width: 1200px; height: 1200px; overflow: hidden;
    background: var(--backdrop);
    font-family: "Raleway", sans-serif;
  }
  .canvas { position: relative; width: 1200px; height: 1200px; }

  .card {
    position: absolute; left: 210px; width: 780px; height: 448px;
    background: var(--card-white);
    box-shadow: 0 6px 18px rgba(0,0,0,0.18);
    overflow: hidden;
  }
  .card--front { top: 136px; }
  .card--back { top: 644px; }

  .band-black { position: absolute; left: 0; width: 100%; background: var(--ink); }
  .band-gold { position: absolute; left: 0; width: 100%; bottom: 0; background: var(--gold); }

  .card--front .band-black { top: 302px; height: 42px; }
  .card--front .band-gold { top: 344px; }

  .brand-name {
    position: absolute; color: var(--ink);
    font-weight: 800; letter-spacing: 0.04em; text-transform: uppercase;
    white-space: nowrap;
  }
  .card--front .brand-name {
    left: 0; width: 100%; top: 170px; text-align: center;
    font-size: 66px; line-height: 1;
  }

  .card--back .band-black { top: 356px; height: 24px; }
  .card--back .band-gold { top: 380px; display: flex; align-items: center; justify-content: center; }
  .tagline { font-size: 23px; font-weight: 600; color: var(--ink); }

  .card--back .brand-name {
    left: 40px; top: 296px; font-size: 30px; line-height: 1;
  }

  .person { position: absolute; left: 364px; top: 60px; }
  .person__name { font-size: 40px; font-weight: 700; color: var(--ink); line-height: 1.1; }
  .person__title { font-size: 25px; font-weight: 400; color: var(--gold-text); margin-top: 2px; }

  .contacts { position: absolute; left: 372px; top: 184px; list-style: none; }
  .contacts li {
    display: flex; align-items: center; height: 30px;
    font-size: 16px; color: var(--grey-text);
  }
  .contacts svg { width: 20px; height: 20px; margin-right: 14px; flex: none; }
  .contacts .label { font-weight: 700; margin-right: 6px; }
  .contacts .value { color: var(--gold-text); }
</style>
</head>
<body>
<main class="canvas">

  <section class="card card--front" aria-label="Business card front">
    <div class="brand-name">The Garb Ledger</div>
    <div class="band-black"></div>
    <div class="band-gold"></div>
  </section>

  <section class="card card--back" aria-label="Business card back">
    <div class="person">
      <h1 class="person__name">Belinda Forsey</h1>
      <p class="person__title">Director and Stylist</p>
    </div>

    <ul class="contacts">
      <li>
        <svg viewBox="0 0 20 20" aria-hidden="true">
          <circle cx="10" cy="10" r="10" fill="var(--ink)"/>
          <path d="M6.5 5.5c.6-.5 1.4-.4 1.7.2l.8 1.5c.2.5.1 1-.3 1.3l-.6.4c.6 1.3 1.6 2.3 2.9 2.9l.4-.6c.3-.4.8-.5 1.3-.3l1.5.8c.6.3.7 1.1.2 1.7l-.6.7c-.6.6-1.6.7-2.4.3-2.6-1.3-4.4-3.1-5.7-5.7-.4-.8-.3-1.8.3-2.4z" fill="#fff"/>
        </svg>
        <span class="label">Telephone :</span><span class="value">+61 8 8217 4592</span>
      </li>
      <li>
        <svg viewBox="0 0 20 20" aria-hidden="true">
          <circle cx="10" cy="10" r="10" fill="var(--ink)"/>
          <rect x="5" y="6.5" width="10" height="7" rx="1" fill="#fff"/>
          <path d="M5.3 7l4.7 3.6L14.7 7" fill="none" stroke="var(--ink)" stroke-width="1.1"/>
        </svg>
        <span class="label">Email :</span><span class="value">belinda@thegarbledger.example</span>
      </li>
      <li>
        <svg viewBox="0 0 20 20" aria-hidden="true">
          <circle cx="10" cy="10" r="10" fill="var(--ink)"/>
          <g fill="none" stroke="#fff" stroke-width="1.1">
            <circle cx="10" cy="10" r="5.2"/>
            <ellipse cx="10" cy="10" rx="2.2" ry="5.2"/>
            <path d="M4.8 10h10.4"/>
          </g>
        </svg>
        <span class="label">website :</span><span class="value">thegarbledger.example</span>
      </li>
    </ul>

    <div class="brand-name">The Garb Ledger</div>
    <div class="band-black"></div>
    <div class="band-gold">
      <p class="tagline">Corporate Workwear &amp; Uniform Specialist | Personal Stylist</p>
    </div>
  </section>

</main>
</body>
</html>
```